IT services company requires Letterhead design

We need a professional letterhead designed to be used for general correspondence with customers, quotes, invoices etc. We are a new IT services company specialising in computer servicing and repairs and mobile and tablet repairs. Attached are templates that my printing company have supplied, my logos, an interpretation of our website for you to get a feel of the company. Details to be included on the letterhead are

Company Number – 4738261
VAT Number - 518337942
Registered Address – 14-16 Brambly Lane, London, E4 9QT

Phone – 01632 487215
Email – sales@quorvent.com
Web – www.quorvent.com

I would prefer for the top of the letterhead to just have the company logo on a white background and the rest of the details on the bottom of the letterhead but I am open to design ideas.

Thanks

```html
<!DOCTYPE html>
<html lang="en">
<head>
<meta charset="utf-8">
<title>Quorvent Letterhead</title>
<link rel="stylesheet" href="https://fonts.googleapis.com/css2?family=Carlito:wght@400;700&display=swap">
<style>
  :root {
    --brand: #2fbfe3;
    --ink: #3a3a3a;
    --body: #555555;
    --paper: #ffffff;
  }
  * { margin: 0; padding: 0; box-sizing: border-box; }
  html, body { width: 800px; height: 1200px; overflow: hidden; background: var(--paper); }
  body { font-family: "Carlito", "Calibri", sans-serif; color: var(--ink); }
  .letterhead { position: relative; width: 800px; height: 1200px; background: var(--paper); overflow: hidden; }

  .brand { position: absolute; left: 58px; top: 34px; display: flex; align-items: center; gap: 10px; }
  .brand-mark { width: 14px; height: 14px; background: var(--brand); }
  .brand-name { font-size: 38px; font-weight: 700; color: var(--brand); line-height: 1; letter-spacing: 0.5px; }

  .registration { position: absolute; right: 49px; top: 42px; text-align: right; font-size: 13px; line-height: 20px; color: var(--ink); }
  .registration .label { color: var(--brand); }

  .header-rule { position: absolute; left: 0; top: 100px; width: 800px; height: 3px; background: var(--brand); }

  .recipient { position: absolute; left: 70px; top: 150px; font-size: 15px; line-height: 28px; color: var(--ink); }
  .recipient .name { font-weight: 700; }

  .salutation { position: absolute; left: 68px; top: 334px; font-size: 17px; font-weight: 700; color: var(--ink); }

  .letter-body { position: absolute; left: 67px; width: 676px; font-size: 12.5px; line-height: 31px; color: var(--body); text-align: justify; }
  .p1 { top: 368px; }
  .p2 { top: 506px; }
  .p3 { top: 620px; }

  .closing { position: absolute; left: 68px; top: 845px; font-size: 15px; color: var(--ink); }
  .closing .signoff { margin-bottom: 14px; }
  .closing .sig-line { line-height: 30px; }
  .closing-right { position: absolute; right: 61px; top: 845px; font-size: 15px; color: var(--ink); }

  .footer-swoosh { position: absolute; left: 0; top: 0; }

  .contact { position: absolute; right: 46px; top: 1102px; list-style: none; font-size: 12.5px; line-height: 18px; color: #ffffff; text-align: right; }
  .contact li { display: flex; justify-content: flex-end; align-items: center; gap: 8px; }
  .contact svg { width: 11px; height: 11px; flex: none; }
</style>
</head>
<body>
<main class="letterhead">
  <div class="brand">
    <span class="brand-name">Quorvent</span>
    <span class="brand-mark"></span>
  </div>

  <div class="registration">
    <p><span class="label">Company Number - </span>4738261</p>
    <p><span class="label">VAT Number - </span>518337942</p>
  </div>

  <div class="header-rule"></div>

  <address class="recipient" style="font-style:normal">
    <p class="name">John Smith</p>
    <p>Owner</p>
    <p>Company Name</p>
    <p>Address Line1, Address Line2</p>
    <p>Country -123456</p>
  </address>

  <h1 class="salutation">Dear John Smith</h1>

  <p class="letter-body p1">Lorem ipsum dolor sit amet, consectetur adipiscing elit, sed do eiusmod tempor incididunt ut labore et dolore magna aliqua. Ut enim ad minim veniam, quis nostrud exercitation ullamco laboris nisi ut aliquip ex ea commodo consequat. Duis aute irure dolor in reprehenderit in voluptate velit esse cillum dolore eu fugiat nulla pariatur. Excepteur sint occaecat cupidatat non proident, sunt in culpa qui officia deserunt mollit anim id est laborum.</p>
  <p class="letter-body p2">Lorem ipsum dolor sit amet, consectetur adipiscing elit, sed do eiusmod tempor incididunt ut labore et dolore magna aliqua. Ut enim ad minim veniam, quis nostrud exercitation ullamco laboris nisi ut aliquip ex ea commodo consequat. Duis aute irure dolor in reprehenderit in voluptate velit esse cillum dolore</p>
  <p class="letter-body p3">Lorem ipsum dolor sit amet, consectetur adipiscing elit, sed do eiusmod tempor incididunt ut labore et dolore magna aliqua. Ut enim ad minim veniam, quis nostrud exercitation ullamco laboris nisi ut aliquip ex ea commodo consequat. Duis aute irure dolor in reprehenderit in voluptate velit esse cillum dolore eu fugiat nulla pariatur. Excepteur sint occaecat cupidatat non proident, sunt in culpa qui officia deserunt mollit anim id est laborum.</p>

  <div class="closing">
    <p class="signoff">Sincerely,</p>
    <p class="sig-line">[ your Name ]</p>
    <p class="sig-line">[ Title ]</p>
  </div>
  <p class="closing-right">Your Faithfully</p>

  <svg class="footer-swoosh" width="800" height="1200" viewBox="0 0 800 1200" aria-hidden="true">
    <path d="M409 1200 Q 710 1100 800 775 L800 1200 Z" fill="var(--brand)"/>
  </svg>

  <ul class="contact">
    <li>01632 487215
      <svg viewBox="0 0 12 12"><path d="M2.5 1 L4.5 1 L5.3 3.4 L4 4.4 Q5 6.8 7.6 8 L8.6 6.7 L11 7.5 L11 9.5 Q10.5 11 9 11 Q1 10 1 2.5 Q1 1 2.5 1 Z" fill="#fff"/></svg>
    </li>
    <li>sales@quorvent.com
      <svg viewBox="0 0 12 12"><rect x="1" y="2.5" width="10" height="7" fill="#fff"/><path d="M1 2.5 L6 6.5 L11 2.5" fill="none" stroke="var(--brand)" stroke-width="1"/></svg>
    </li>
    <li>www.quorvent.com
      <svg viewBox="0 0 12 12"><g fill="none" stroke="#fff" stroke-width="1"><circle cx="6" cy="6" r="5"/><ellipse cx="6" cy="6" rx="2.2" ry="5"/><path d="M1 6 H11"/></g></svg>
    </li>
    <li>14-16 Brambly Lane, London, E4 9QT
      <svg viewBox="0 0 12 12"><path d="M6 11.5 Q2 7 2 4.5 A4 4 0 0 1 10 4.5 Q10 7 6 11.5 Z" fill="#fff"/><circle cx="6" cy="4.5" r="1.5" fill="var(--brand)"/></svg>
    </li>
  </ul>
</main>
</body>
</html>
```